Letter Head Design

I need a letter head design based on my company logo that I attached.
Include phone number: (403)582-4316
Address: 347 14th Avenue NE, Calgary, Alberta, Canada, T3K 4R8

Industry/Entity Type

It Company

```html
<!DOCTYPE html>
<html lang="en">
<head>
<meta charset="utf-8">
<title>BrightNest Interiors Corp. — Letterhead</title>
<link rel="stylesheet" href="https://fonts.googleapis.com/css2?family=PT+Sans:wght@400;700&family=PT+Sans+Narrow:wght@700&display=swap">
<style>
  :root {
    --brand-blue: #1f5fae;
    --brand-blue-dark: #12468a;
    --brand-green: #5aac3c;
    --ink: #333333;
    --paper: #ffffff;
    --wash-green: #f3f8ef;
    --wash-blue: #eef4fb;
  }
  html, body {
    margin: 0;
    padding: 0;
    overflow: hidden;
    background: var(--paper);
  }
  .letterhead {
    position: relative;
    width: 867px;
    height: 1200px;
    overflow: hidden;
    background: var(--paper);
    font-family: "PT Sans", Arial, sans-serif;
    color: var(--ink);
  }
  .letterhead__wash {
    position: absolute;
    left: 12px;
    top: 285px;
    width: 843px;
    height: 880px;
    border-radius: 40px;
    background: linear-gradient(90deg, var(--wash-green) 0%, #ffffff 45%, var(--wash-blue) 100%);
    opacity: 0.7;
  }
  .brand {
    position: absolute;
    left: 96px;
    top: 20px;
    width: 240px;
    text-align: center;
  }
  .brand__square {
    display: block;
    width: 132px;
    height: 132px;
    margin: 0 auto 20px;
    border-radius: 6px;
    background: var(--brand-green);
  }
  .brand__name {
    display: block;
    font-family: "PT Sans Narrow", "PT Sans", Arial, sans-serif;
    font-weight: 700;
    font-size: 56px;
    line-height: 1;
    letter-spacing: -1px;
    color: var(--brand-blue);
    white-space: nowrap;
  }
  .brand__tagline {
    display: block;
    margin-top: 4px;
    padding-left: 120px;
    text-align: left;
    font-size: 11px;
    color: var(--brand-blue);
  }
  .contact {
    position: absolute;
    left: 481px;
    top: 44px;
    font-size: 29px;
    line-height: 41px;
    letter-spacing: -0.3px;
  }
  .contact__address { margin: 0; }
  .contact__phone {
    margin: 49px 0 0 4px;
  }
  .divider {
    position: absolute;
    top: 266px;
    left: 0;
    width: 867px;
    height: 6px;
    display: flex;
  }
  .divider__green { width: 431px; background: var(--brand-green); }
  .divider__blue { flex: 1; background: var(--brand-blue); }
  .footer-band {
    position: absolute;
    left: 0;
    bottom: 0;
    width: 867px;
    height: 8px;
    background: var(--brand-blue);
  }
  .footer-tab {
    position: absolute;
    right: 0;
    bottom: 6px;
    width: 305px;
    height: 95px;
  }
  .footer-tab svg { display: block; }
  .footer-tab__brand {
    position: absolute;
    left: 84px;
    top: 26px;
    display: flex;
    align-items: center;
    gap: 10px;
    font-weight: 700;
    font-size: 27px;
    color: var(--paper);
    white-space: nowrap;
  }
  .footer-tab__square {
    width: 40px;
    height: 40px;
    border-radius: 4px;
    background: var(--paper);
  }
</style>
</head>
<body>
  <main class="letterhead">
    <div class="letterhead__wash" aria-hidden="true"></div>

    <header>
      <div class="brand">
        <span class="brand__square" aria-hidden="true"></span>
        <span class="brand__name">BrightNest</span>
        <span class="brand__tagline">Interiors Corp.</span>
      </div>

      <address class="contact" style="font-style: normal;">
        <p class="contact__address">347 14th Avenue NE, Calgary,<br>Alberta, Canada, T3K 4R8</p>
        <p class="contact__phone">Tel: (403)582-4316</p>
      </address>

      <div class="divider" aria-hidden="true">
        <span class="divider__green"></span>
        <span class="divider__blue"></span>
      </div>
    </header>

    <footer>
      <div class="footer-tab">
        <svg width="305" height="95" viewBox="0 0 305 95" aria-hidden="true">
          <defs>
            <linearGradient id="tabFill" x1="0" y1="0" x2="1" y2="1">
              <stop offset="0" stop-color="#2a72c4"/>
              <stop offset="1" stop-color="#12468a"/>
            </linearGradient>
          </defs>
          <path d="M95 0 H305 V95 H0 Z" fill="url(#tabFill)"/>
        </svg>
        <div class="footer-tab__brand">
          <span class="footer-tab__square" aria-hidden="true"></span>
          <span>BrightNest</span>
        </div>
      </div>
      <div class="footer-band" aria-hidden="true"></div>
    </footer>
  </main>
</body>
</html>
```